Author needs website header

I want a website header that shows me as an author with a attractive tagline and highlights my new book with a Call to Action to get a Free Chapter

Industry/Entity Type

Call

```html
<!DOCTYPE html>
<html lang="en">
<head>
<meta charset="utf-8">
<title>Heeding the Voice of Grace — Author Header</title>
<link href="https://fonts.googleapis.com/css2?family=Forum&family=Lora:wght@400&family=Great+Vibes&display=swap" rel="stylesheet">
<style>
  :root {
    --stage: #575757;
    --navy: #0b1522;
    --navy-mid: #10243a;
    --teal: #6fd6dc;
    --teal-deep: #12a9b8;
    --field-teal: #13b3c4;
    --white: #ffffff;
    --orange: #f57c00;
    --orange-light: #ff8f1a;
    --ink: #1b1208;
    --placeholder: #9a9a9a;
  }
  * { margin: 0; padding: 0; box-sizing: border-box; }
  html, body { width: 1200px; height: 1200px; overflow: hidden; background: var(--stage); }
  .header-banner {
    position: absolute; left: 56px; top: 250px; width: 1088px; height: 700px;
    overflow: hidden;
    background:
      radial-gradient(ellipse 260px 200px at 820px 40px, rgba(18,169,184,.85), rgba(18,169,184,0) 100%),
      radial-gradient(circle 90px at 120px 560px, rgba(30,70,100,.35), transparent),
      radial-gradient(circle 70px at 60px 140px, rgba(30,70,100,.3), transparent),
      radial-gradient(circle 60px at 300px 80px, rgba(30,70,100,.25), transparent),
      linear-gradient(180deg, var(--navy-mid) 0%, var(--navy) 70%);
  }
  .headline {
    position: absolute; left: 66px; top: 58px; z-index: 2;
    display: flex; align-items: baseline; gap: 12px;
    font-family: "Forum", serif; font-weight: 400; color: var(--white); white-space: nowrap;
  }
  .headline .lead { font-size: 56px; }
  .headline .mid { font-size: 42px; }
  .headline .accent { font-size: 78px; color: var(--teal); }
  .book-stack {
    position: absolute; left: 48px; top: 150px; width: 332px; height: 416px;
    background: linear-gradient(160deg, #e9f2fb 0%, #bcd6ee 55%, #7fae5a 100%);
    border-radius: 3px; opacity: .95;
  }
  .order-badge {
    position: absolute; left: 362px; top: 460px; width: 88px; height: 88px; z-index: 2;
    border-radius: 50%; background: var(--teal-deep);
    display: flex; flex-direction: column; align-items: center; justify-content: center;
    font-family: "Great Vibes", cursive; color: var(--white); font-size: 30px; line-height: .95;
  }
  .tagline {
    position: absolute; left: 392px; top: 222px; width: 320px; text-align: center; z-index: 2;
    font-family: "Lora", serif; color: var(--white); font-size: 35px; line-height: 36px;
  }
  .tagline p + p { margin-top: 38px; }
  .author-photo {
    position: absolute; left: 696px; top: 0; width: 392px; height: 700px;
    background: linear-gradient(180deg, #2a2320 0%, #6b4a38 35%, #b9c6d6 70%, #0f1a27 100%);
    clip-path: polygon(35% 0, 100% 0, 100% 100%, 0 100%, 4% 60%, 22% 42%);
  }
  .signup-field {
    position: absolute; top: 592px; height: 32px; background: var(--field-teal);
  }
  .signup-field .input {
    position: absolute; top: 0; height: 32px; background: var(--white);
    display: flex; align-items: center; gap: 18px; padding-left: 12px;
    font-family: "Lora", serif; font-size: 21px; color: var(--placeholder);
  }
  .field-name { left: 62px; width: 312px; }
  .field-name .input { left: 10px; width: 278px; padding-left: 6px; }
  .field-email { left: 416px; width: 308px; }
  .field-email .input { left: 11px; width: 276px; }
  .submit-button {
    position: absolute; left: 738px; top: 576px; width: 266px; height: 64px; z-index: 2;
    border-radius: 32px; background: linear-gradient(180deg, var(--orange-light), var(--orange));
    font-family: "Forum", serif; font-size: 42px; color: var(--ink);
    display: flex; align-items: center; justify-content: center; padding-top: 4px;
  }
  .free-offer {
    position: absolute; left: 394px; top: 644px; width: 300px; text-align: center;
    font-family: "Lora", serif; font-size: 22px; color: var(--orange);
  }
</style>
</head>
<body>
  <section class="header-banner">
    <div class="book-stack" role="img" aria-label="Three copies of the book Heeding the Voice of Grace by Marisol Ebanks, cover with sky and meadow"></div>
    <div class="author-photo" role="img" aria-label="Portrait of the author Marisol Ebanks, smiling, wearing a light patterned jacket"></div>

    <h1 class="headline">
      <span class="lead">HEEDING</span><span class="mid">THE VOICE OF</span><span class="accent">GRACE</span>
    </h1>

    <div class="order-badge"><span>Order</span><span>Now</span></div>

    <div class="tagline">
      <p>A journey in discovering divine</p>
      <p>opportunities in unexpected places</p>
    </div>

    <div class="signup-field field-name"><div class="input">Name</div></div>
    <div class="signup-field field-email">
      <div class="input">
        <svg width="22" height="16" viewBox="0 0 22 16" aria-hidden="true">
          <rect x="1" y="1" width="20" height="14" fill="none" stroke="#8a8a8a" stroke-width="1.4"/>
          <path d="M1 1 L11 9 L21 1" fill="none" stroke="#8a8a8a" stroke-width="1.4"/>
        </svg>
        <span>Email Address</span>
      </div>
    </div>
    <div class="submit-button">SUBMIT</div>
    <p class="free-offer">Get My eBook For Free</p>
  </section>
</body>
</html>
```